Business Card Design

Need a card designed to fit the tax preparation and accounting profession. Would like to include the following on side two of the card:

Tax Preparation and Audit Representation for:
Individuals
Partnerships
Corporations
Estates
Trusts
Other entities with tax reporting requirements

Industry/Entity Type

Accounting

Contact Information for Business Card

Marlowe & Associates
Tax and Business Services
Derek P Halvorsen II, EA, MS
Enrolled Agent P07385169
4172 Sorrel Avenue, Suite B
Citrus Heights, CA 95847
(916) 284-6051
Email: ledgerpro782@mailbrook.net
www.ledgerhelpcenter.net

```html
<!DOCTYPE html>
<html lang="en">
<head>
<meta charset="utf-8">
<title>Marlowe &amp; Associates — Business Card</title>
<link rel="stylesheet" href="https://fonts.googleapis.com/css2?family=Open+Sans:wght@400;600&display=swap">
<style>
  :root {
    --brand-blue: #2aace2;
    --paper: #ffffff;
    --ink: #3a3a3a;
    --ink-soft: #555555;
    --backdrop: #dcdde0;
  }
  * { box-sizing: border-box; margin: 0; padding: 0; }
  html, body { width: 1200px; height: 988px; overflow: hidden; }
  body {
    background: var(--backdrop);
    font-family: "Open Sans", Arial, sans-serif;
    display: flex;
    flex-direction: column;
    align-items: center;
    justify-content: center;
    gap: 56px;
  }
  .card {
    position: relative;
    width: 660px;
    height: 377px;
    background: var(--paper);
    box-shadow: 0 6px 18px rgba(0,0,0,0.18);
    overflow: hidden;
  }

  /* Back side */
  .card-back .band { position: absolute; left: 0; right: 0; background: var(--brand-blue); }
  .card-back .band-top { top: 30px; height: 84px; }
  .card-back .band-bottom {
    top: 258px; height: 84px;
    display: flex; flex-direction: column; justify-content: center; align-items: center;
    color: var(--paper); font-size: 12px; line-height: 1.45; text-align: center;
  }
  .services .services-lead { font-weight: 600; }
  .card-back .brand {
    position: absolute; left: 0; right: 0; top: 114px; height: 144px;
    display: flex; flex-direction: column; justify-content: center; align-items: center;
    color: var(--brand-blue); font-size: 27px; line-height: 1.2; text-align: center;
  }

  /* Front side */
  .card-front .band-title {
    position: absolute; left: 0; top: 26px; width: 460px; height: 150px;
    background: var(--brand-blue); color: var(--paper);
    display: flex; flex-direction: column; justify-content: center; align-items: center;
    font-size: 26px; line-height: 1.2; text-align: center;
  }
  .card-front .holder {
    position: absolute; left: 110px; top: 194px; width: 360px; text-align: center;
  }
  .holder .name { font-size: 15px; font-weight: 600; letter-spacing: 1px; color: var(--ink); }
  .holder .role { font-size: 10px; letter-spacing: 1px; color: var(--ink-soft); }
  .contacts {
    position: absolute; left: 96px; top: 248px;
    display: grid; grid-template-columns: 150px 210px; row-gap: 9px; column-gap: 16px;
    font-size: 11px; color: var(--ink-soft);
  }
  .contact { display: flex; align-items: center; gap: 6px; white-space: nowrap; }
  .contact svg { width: 13px; height: 13px; flex: none; }
  .contact.address { grid-column: 1 / 3; padding-left: 19px; }
  .rule { position: absolute; left: 22px; right: 22px; background: var(--brand-blue); }
  .rule-thick { top: 336px; height: 5px; }
  .rule-thin { top: 346px; height: 2px; }
</style>
</head>
<body>

<section class="card card-back" aria-label="Card back">
  <div class="band band-top"></div>
  <div class="brand">
    <span>Marlowe &amp; Associates</span>
    <span>Tax and Business Services</span>
  </div>
  <div class="band band-bottom services">
    <p class="services-lead">Tax Preparation and Audit Representation for:</p>
    <p>Individuals · Partnerships · Corporations · Estates · Trusts</p>
    <p>Other entities with tax reporting requirements</p>
  </div>
</section>

<section class="card card-front" aria-label="Card front">
  <div class="band-title">
    <span>Marlowe &amp; Associates</span>
    <span>Tax and Business Services</span>
  </div>
  <div class="holder">
    <p class="name">DEREK P HALVORSEN II, EA, MS</p>
    <p class="role">ENROLLED AGENT P07385169</p>
  </div>
  <div class="contacts">
    <p class="contact">
      <svg viewBox="0 0 14 14"><circle cx="7" cy="7" r="7" fill="var(--brand-blue)"/><path d="M4.6 3.6l1.3 1.5-.7.9c.5 1 1.3 1.8 2.3 2.3l.9-.7 1.5 1.3-.8 1.2C6.8 9.8 4.2 7.2 3.9 4.4z" fill="#fff"/></svg>
      (916) 284-6051
    </p>
    <p class="contact">
      <svg viewBox="0 0 14 14"><circle cx="7" cy="7" r="7" fill="var(--brand-blue)"/><circle cx="7" cy="7" r="3.6" fill="none" stroke="#fff" stroke-width="0.9"/><path d="M3.4 7h7.2M7 3.4v7.2" stroke="#fff" stroke-width="0.8"/></svg>
      www.ledgerhelpcenter.net
    </p>
    <p class="contact">
      <svg viewBox="0 0 14 14"><circle cx="7" cy="7" r="7" fill="var(--brand-blue)"/><rect x="3.5" y="4.5" width="7" height="5" fill="#fff"/><path d="M3.5 4.5L7 7.3l3.5-2.8" fill="none" stroke="var(--brand-blue)" stroke-width="0.8"/></svg>
      ledgerpro782@mailbrook.net
    </p>
    <p class="contact"></p>
    <p class="contact address">4172 Sorrel Avenue, Suite B, Citrus Heights, CA 95847</p>
  </div>
  <div class="rule rule-thick"></div>
  <div class="rule rule-thin"></div>
</section>

</body>
</html>
```